Forge Night Club Flyer, need asap for party this weekend

Need a flyer for club night this Saturday. Guaranteed project need quick turnaround. Image attached, and the FORGE logo to be large and detailed like a sign. The dj names MERIDAN, MR. KALTOVE, AND DESMOND R. FALLOWAY can be large too. It's for house/electronic music in a nice classy venue. High Res image attached.

Target Market(s)

21-40 year old house music lovers, club business

Industry/Entity Type

Night Club

Font styles to use
Sans Serif

Colors
ffffff
cadf82
33a6d7
0356a4
fbee3d

Requirements
Must have
• Either the girl in hard hat or tool belt image, or something similar to stick with the Forge theme. Also the dj names needs to be the same size
Nice to have
• Faded image or some lining around the images so it doesn't look like a plain photo. Black and white is good or faded.
Should not have
• Any cursive or anything not professional looking

```html
<!DOCTYPE html>
<html lang="en">
<head>
<meta charset="utf-8">
<title>Forge Club Night Flyer</title>
<link rel="stylesheet" href="https://fonts.googleapis.com/css2?family=Montserrat:wght@500;700;800&display=swap">
<style>
  :root {
    --stage: #2b1d17;
    --white: #ffffff;
    --lime: #cadf82;
    --sky: #33a6d7;
    --royal: #0356a4;
    --yellow: #fbee3d;
    --navy: #061a3d;
    --band: #041430;
    --lilac: #b9a6e6;
  }
  * { margin: 0; padding: 0; box-sizing: border-box; }
  html, body {
    width: 1200px; height: 1105px; overflow: hidden;
    background: var(--stage);
  }
  .flyer {
    position: absolute; left: 250px; top: 58px;
    width: 700px; height: 990px; overflow: hidden;
    background:
      radial-gradient(circle at 82% 30%, rgba(51,166,215,.55), transparent 40%),
      radial-gradient(circle at 75% 58%, rgba(202,223,130,.18), transparent 40%),
      linear-gradient(180deg, var(--sky) 0%, var(--royal) 48%, var(--navy) 78%, #030c22 100%);
    font-family: "Montserrat", sans-serif;
  }
  .photo {
    position: absolute; left: 0; top: 0; width: 410px; height: 760px;
    background:
      linear-gradient(180deg, transparent 62%, rgba(6,26,61,.95) 100%),
      linear-gradient(90deg, transparent 78%, rgba(3,86,164,.7) 100%),
      linear-gradient(165deg, #8fdcf2 0%, var(--sky) 30%, var(--lilac) 58%, var(--royal) 85%);
  }
  .photo-frame {
    position: absolute; left: 14px; top: 14px; width: 382px; height: 700px;
    border: 2px solid rgba(255,255,255,.55);
    border-bottom-color: transparent;
  }
  .band { position: absolute; left: 0; top: 0; width: 700px; height: 990px; }
  .logo {
    position: absolute; left: 565px; top: 150px;
    transform: translate(-50%, -50%) rotate(48deg);
    font-size: 84px; font-weight: 800; letter-spacing: 6px;
    color: var(--white); white-space: nowrap; line-height: 1;
  }
  .lineup {
    position: absolute; left: 410px; top: 430px; width: 280px;
    text-align: center; line-height: 1.08;
  }
  .lineup .tagline {
    font-size: 32px; font-weight: 800; color: var(--lime);
    margin-bottom: 18px;
  }
  .lineup .dj {
    font-size: 28px; font-weight: 700; color: var(--white);
    margin-bottom: 6px;
  }
  .details {
    position: absolute; left: 0; top: 790px; width: 700px;
    text-align: center; color: var(--white);
  }
  .details .when { font-size: 26px; font-weight: 700; color: var(--yellow); }
  .details .venue { font-size: 40px; font-weight: 800; margin-top: 12px; }
  .details .address { font-size: 30px; font-weight: 500; margin-top: 6px; }
  .details .entry { font-size: 18px; font-weight: 700; margin-top: 16px; color: var(--lime); }
</style>
</head>
<body>
  <main class="flyer">
    <div class="photo" role="img" aria-label="Faded photo of a torso wearing a leather tool belt full of wrenches and pliers, above a silhouetted dancing crowd, tinted blue"></div>
    <div class="photo-frame" aria-hidden="true"></div>
    <svg class="band" viewBox="0 0 700 990" aria-hidden="true">
      <polygon points="340,0 520,0 700,200 700,400" fill="var(--band)"/>
      <line x1="520" y1="0" x2="700" y2="200" stroke="var(--sky)" stroke-width="2"/>
      <line x1="340" y1="0" x2="700" y2="400" stroke="var(--sky)" stroke-width="2"/>
    </svg>
    <h1 class="logo">FORGE</h1>
    <section class="lineup">
      <p class="tagline">W/HOUSE &amp;<br>TECH<br>WORKERS</p>
      <p class="dj">MERIDAN</p>
      <p class="dj">MR. KALTOVE</p>
      <p class="dj">DESMOND R.<br>FALLOWAY</p>
    </section>
    <section class="details">
      <p class="when">21+ • SAT 3/12/16 • 10PM TO 2AM</p>
      <p class="venue">HALVERN LOUNGE</p>
      <p class="address">418 W. Larkspur Ave, Dunmore</p>
      <p class="entry">NO COVER W/ RSVP</p>
    </section>
  </main>
</body>
</html>
```